Etiketten für Obsthof in Friedrichshafen am Bodensee
Zielgruppe
Wir sind ein Obsthof in Friedrichshafen am Bodensee und verkaufen in unserem Hofladen unsere selbsthergestellten Produkte. Dabei zeichnet uns besonders aus, dass wir unsere Produkte aus eigens angebautem Obst Herstellen wie zum Beispiel Marmeladen, Säfte, Sirup, Schnaps oder Liköre.
Unsere Zielgruppe sind Kundinnen und Kunden, die Wert auf Regionalität, Transparenz bei der Produktherstellung und Qualität der Inhaltsstoffe legen.
Aufgabenstellung
Uns ist besonders wichtig, dass die Etiketten widerspiegeln, dass die Produkte selbst hergestellt wurden und hochwertig sind.
Die Etiketten sollten alle auf einander abgestimmt sein, sodass sie sich wie eine klare Linie durch das ganze Sortiment ziehen. Dementsprechend soll ein universelles Etikett erstellt werden, das wir für alle unsere Produkte verwenden können. Hierbei ist es wichtig, dass wir im Nachhinein selbst die Produktbeschreibung auf dem Etikett an das jeweilige Produkt anpassen können.
Es sollte auch Platz sein für die Inhaltsstoffe, unsere Anschrift, Mindesthaltbarkeitsdatum und die Inhaltsmenge.
https://www.wendrahof-polmit.com/hofladen-und-produkte.htm
in diese Richtung könnte ich mir die Ausführung vorstellen.

```html
<!DOCTYPE html>
<html lang="de">
<head>
<meta charset="utf-8">
<title>Lindar Obsthof – Etikettenlinie</title>
<link rel="stylesheet" href="https://fonts.googleapis.com/css2?family=Amatic+SC:wght@700&family=Fredoka:wght@600&family=Roboto+Condensed:wght@300&display=swap">
<style>
  :root {
    --canvas: #f2f2f2;
    --label: #ffffff;
    --ink: #4a4a4a;
    --ink-soft: #8a8a8a;
    --copper: #b46e4c;
    --copper-dark: #8a4528;
    --copper-light: #e6bfa6;
  }
  * { margin: 0; padding: 0; box-sizing: border-box; }
  html, body { width: 1200px; height: 849px; overflow: hidden; }
  body { background: var(--canvas); position: relative; font-family: "Roboto Condensed", sans-serif; }

  .label {
    position: absolute;
    background: var(--label);
    border-radius: 14px;
    box-shadow: 0 2px 8px rgba(0,0,0,.08);
    display: flex; flex-direction: column; align-items: center;
    overflow: hidden;
  }
  .label--sirup  { left: 140px; top: 530px; width: 188px; height: 200px; }
  .label--likoer { left: 547px; top: 479px; width: 154px; height: 226px; }
  .label--jam    { left: 917px; top: 544px; width: 188px; height: 198px; }

  .label__band {
    width: 100%; height: 18px; flex: none;
    background: linear-gradient(90deg, var(--copper-dark), var(--copper), var(--copper-light), var(--copper), var(--copper-dark), var(--copper-light), var(--copper));
    opacity: .85;
  }
  .label__body {
    flex: 1; width: 100%;
    display: flex; flex-direction: column; align-items: center; justify-content: space-evenly;
    padding: 4px 14px;
  }
  .brand { display: flex; align-items: center; gap: 5px; }
  .brand__dot { width: 16px; height: 16px; border-radius: 50%; background: var(--copper); }
  .brand__name {
    font-family: "Fredoka", sans-serif; font-weight: 600; font-size: 15px;
    color: var(--copper); line-height: 1; letter-spacing: .3px;
  }
  .tagline { width: 100%; height: 22px; display: block; }
  .tagline text { font-family: "Roboto Condensed", sans-serif; font-size: 7px; fill: var(--ink-soft); letter-spacing: .4px; }
  .product {
    font-family: "Amatic SC", sans-serif; font-weight: 700;
    color: var(--ink); font-size: 31px; line-height: .95; text-align: center; letter-spacing: 1px;
  }
  .label--likoer .product { font-size: 30px; }
  .amount {
    width: 100%; display: flex; align-items: center; gap: 6px;
    font-size: 11px; color: var(--ink-soft); letter-spacing: .5px;
  }
  .amount::before, .amount::after {
    content: ""; flex: 1; border-top: 1.5px dotted var(--copper-light);
  }
</style>
</head>
<body>

<svg width="0" height="0" style="position:absolute">
  <defs>
    <path id="arc" d="M30 20 Q75 2 120 20"/>
  </defs>
</svg>

<article class="label label--sirup">
  <div class="label__band" role="img" aria-label="Band aus kleinen kupferfarbenen Äpfeln"></div>
  <div class="label__body">
    <div class="brand"><span class="brand__dot"></span><span class="brand__name">LINDAR Obsthof</span></div>
    <svg class="tagline" viewBox="0 0 150 22" preserveAspectRatio="none">
      <line x1="2" y1="19" x2="28" y2="19" stroke="#e6bfa6" stroke-dasharray="1.5 2"/>
      <line x1="122" y1="19" x2="148" y2="19" stroke="#e6bfa6" stroke-dasharray="1.5 2"/>
      <text><textPath href="#arc" startOffset="50%" text-anchor="middle">100% aus eigenem Anbau</textPath></text>
    </svg>
    <h2 class="product">HOLUNDER<br>SIRUP</h2>
    <p class="amount">350 ML ℮</p>
  </div>
  <div class="label__band" role="img" aria-label="Band aus kleinen kupferfarbenen Äpfeln"></div>
</article>

<article class="label label--likoer">
  <div class="label__band" role="img" aria-label="Band aus kleinen kupferfarbenen Äpfeln"></div>
  <div class="label__body">
    <div class="brand"><span class="brand__dot"></span><span class="brand__name">LINDAR Obsthof</span></div>
    <svg class="tagline" viewBox="0 0 150 22" preserveAspectRatio="none">
      <line x1="2" y1="19" x2="28" y2="19" stroke="#e6bfa6" stroke-dasharray="1.5 2"/>
      <line x1="122" y1="19" x2="148" y2="19" stroke="#e6bfa6" stroke-dasharray="1.5 2"/>
      <text><textPath href="#arc" startOffset="50%" text-anchor="middle">100% aus eigenem Anbau</textPath></text>
    </svg>
    <h2 class="product">WALNUSS<br>LIKÖR</h2>
    <p class="amount">350 ML ℮</p>
  </div>
  <div class="label__band" role="img" aria-label="Band aus kleinen kupferfarbenen Äpfeln"></div>
</article>

<article class="label label--jam">
  <div class="label__band" role="img" aria-label="Band aus kleinen kupferfarbenen Äpfeln"></div>
  <div class="label__body">
    <div class="brand"><span class="brand__dot"></span><span class="brand__name">LINDAR Obsthof</span></div>
    <svg class="tagline" viewBox="0 0 150 22" preserveAspectRatio="none">
      <line x1="2" y1="19" x2="28" y2="19" stroke="#e6bfa6" stroke-dasharray="1.5 2"/>
      <line x1="122" y1="19" x2="148" y2="19" stroke="#e6bfa6" stroke-dasharray="1.5 2"/>
      <text><textPath href="#arc" startOffset="50%" text-anchor="middle">100% aus eigenem Anbau</textPath></text>
    </svg>
    <h2 class="product">SAUERKIRSCH<br>KONFITÜRE</h2>
    <p class="amount">350 ML ℮</p>
  </div>
  <div class="label__band" role="img" aria-label="Band aus kleinen kupferfarbenen Äpfeln"></div>
</article>

</body>
</html>
```